Android app task management design

We have an android app that needs improvement in design. We have used a color pallet that we'd like to continue to use (attached). I have attached files of how the app is now, how someone else tried to improve the design (downloads file) and a report that also needs a redesign (the pdf). We'd like the design to be more modern, fresh and professional. The app is used by gas stations, hotels, restaurants and other companies that need HACCP registration because of food regulations. The app will be mostly used on tablets.
Target Market(s)
Gas stations, hotels, restaurants
Industry/Entity Type
Digital
Requirements
Must have
- A professional and clear user interface with a modern look that will last long. It must have colors from the color pallet attached.
Nice to have
- The fox attached. (Name: Tidy wren)

```html
<!DOCTYPE html>
<html lang="nl">
<head>
<meta charset="utf-8">
<title>Tidy wren – taken app</title>
<link href="https://fonts.googleapis.com/css2?family=Poppins:wght@400;500;600&display=swap" rel="stylesheet">
<style>
:root{
  --bg:#ffffff;
  --card:#ffffff;
  --blue:#1f9be3;
  --blue-deep:#2a66b4;
  --ink:#1e56a0;
  --muted:#8fa6c4;
  --line:#9cc3e8;
  --orange:#f7a012;
  --shadow:0 6px 28px rgba(40,80,140,.10);
}
*{box-sizing:border-box;margin:0;padding:0}
html,body{width:912px;height:1200px;overflow:hidden;background:var(--bg);font-family:"Poppins",sans-serif;color:var(--ink)}
.canvas{position:relative;width:912px;height:1200px}
.screen{position:absolute;background:var(--card);border-radius:26px;box-shadow:var(--shadow);overflow:hidden}
.abs{position:absolute}

/* login */
.login{left:36px;top:25px;width:312px;height:555px}
.mascot{left:10px;top:25px;width:158px;height:219px;border-radius:50% 50% 40% 40%;background:radial-gradient(circle at 45% 40%,#e98b3d,#b65a1f 55%,#3f9be0 80%,#fff 100%)}
.band{left:0;top:302px;width:22px;height:253px;background:var(--blue);border-radius:0 14px 0 0}
.band-low{left:0;top:427px;width:22px;height:128px;background:var(--blue-deep);border-radius:0 14px 0 0}
.tab{top:298px;font-size:11px;font-weight:500}
.tab.active{left:152px;width:70px;text-align:center;font-weight:600;border-bottom:2px solid var(--ink);padding-bottom:5px}
.tab.plain{left:241px}
.field{left:111px;width:190px;border-bottom:1px solid var(--line);font-size:11px;color:var(--muted);padding-bottom:3px}
.btn-login{left:229px;top:466px;width:72px;height:23px;border-radius:12px;background:var(--blue-deep);color:#fff;font-size:11px;font-weight:500;display:flex;align-items:center;justify-content:space-between;padding:0 9px 0 14px}

/* staff list */
.staff{left:557px;top:36px;width:311px;height:557px}
.menu{width:17px;height:12px}
.topbar-title{font-size:13px;font-weight:500}
.search{left:43px;top:77px;width:227px;height:34px;border-radius:17px;box-shadow:0 3px 12px rgba(40,80,140,.13);display:flex;align-items:center;justify-content:space-between;padding:0 14px 0 22px;font-size:7.5px}
.row{left:20px;width:280px;height:61px;display:flex;align-items:center}
.avatar{width:61px;height:61px;border-radius:50%;flex:none}
.name{margin-left:14px;font-size:13px;font-weight:500;flex:1;white-space:nowrap}
.dot{width:28px;height:28px;border-radius:50%;display:flex;align-items:center;justify-content:center;flex:none;margin-left:13px}
.dot.orange{background:var(--orange)}
.dot.blue{background:var(--blue)}

/* tasks */
.tasks{left:273px;top:623px;width:311px;height:560px;border-radius:26px 26px 0 0}
.head-avatar{left:15px;top:63px;width:61px;height:61px;border-radius:50%;background:radial-gradient(circle at 50% 40%,#c9a38a,#4a3a33 70%)}
.head-name{left:90px;top:78px;font-size:13px;font-weight:500}
.head-date{left:90px;top:97px;font-size:7px;color:#7a8aa3}
.head-check{left:258px;top:79px}
.gauge{width:80px;text-align:center}
.gauge svg{display:block;margin:0 auto}
.gauge .pct{position:absolute;left:0;top:42px;width:80px;font-size:14px;font-weight:600;color:#fff}
.gauge .label{font-size:7.5px;line-height:1.2;margin-top:6px;white-space:nowrap}
</style>
</head>
<body>
<div class="canvas">

  <section class="screen login">
    <div class="abs mascot" role="img" aria-label="Illustratie van de Tidy wren mascotte in heldenpose met blauwe cape"></div>
    <div class="abs band"></div>
    <div class="abs band-low"></div>
    <div class="abs tab active">Manager</div>
    <div class="abs tab plain">Reviews</div>
    <div class="abs field" style="top:368px">Email</div>
    <div class="abs field" style="top:416px">Wachtwoord</div>
    <div class="abs btn-login">Login
      <svg width="6" height="9" viewBox="0 0 6 9"><path d="M1 1l3.5 3.5L1 8" fill="none" stroke="#fff" stroke-width="1.4"/></svg>
    </div>
  </section>

  <section class="screen staff">
    <svg class="abs menu" style="left:17px;top:24px" viewBox="0 0 17 12"><path d="M0 1h17M0 6h12M0 11h17" stroke="var(--ink)" stroke-width="1.6"/></svg>
    <div class="abs topbar-title" style="left:60px;top:21px">Test Locatie</div>
    <div class="abs search"><span>Werknemer zoeken</span>
      <svg width="15" height="15" viewBox="0 0 15 15"><circle cx="6" cy="6" r="4.7" fill="none" stroke="var(--ink)" stroke-width="1.7"/><path d="M9.5 9.5L14 14" stroke="var(--ink)" stroke-width="1.8"/></svg>
    </div>

    <div class="abs row" style="top:139px">
      <div class="avatar" role="img" aria-label="Profielfoto medewerker" style="background:radial-gradient(circle at 50% 45%,#f1d2bd,#c9a38a 60%,#eee 100%)"></div>
      <div class="name">Lotte Vermaas</div>
      <div class="dot orange"><svg width="14" height="14" viewBox="0 0 14 14"><circle cx="7" cy="7" r="5.8" fill="none" stroke="#fff" stroke-width="1.3"/><path d="M4.3 7.2l2 2 3.6-4" fill="none" stroke="#fff" stroke-width="1.3"/></svg></div>
      <div class="dot blue"><svg width="12" height="14" viewBox="0 0 12 14"><rect x="1" y="2" width="10" height="11.5" rx="1.5" fill="#fff"/><rect x="4" y="0.5" width="4" height="3" rx="1" fill="#fff" stroke="var(--blue)" stroke-width=".8"/><path d="M3.5 6.5h5M3.5 9h5M3.5 11.3h5" stroke="var(--blue)" stroke-width="1"/></svg></div>
    </div>
    <div class="abs row" style="top:224px">
      <div class="avatar" role="img" aria-label="Profielfoto medewerker" style="background:radial-gradient(circle at 50% 40%,#b08a72,#3d3029 60%,#6b5a4d 100%)"></div>
      <div class="name">Marieke Dolder</div>
      <div class="dot orange"><svg width="14" height="14" viewBox="0 0 14 14"><circle cx="7" cy="7" r="5.8" fill="none" stroke="#fff" stroke-width="1.3"/><path d="M4.3 7.2l2 2 3.6-4" fill="none" stroke="#fff" stroke-width="1.3"/></svg></div>
      <div class="dot blue"><svg width="12" height="14" viewBox="0 0 12 14"><rect x="1" y="2" width="10" height="11.5" rx="1.5" fill="#fff"/><rect x="4" y="0.5" width="4" height="3" rx="1" fill="#fff" stroke="var(--blue)" stroke-width=".8"/><path d="M3.5 6.5h5M3.5 9h5M3.5 11.3h5" stroke="var(--blue)" stroke-width="1"/></svg></div>
    </div>
    <div class="abs row" style="top:309px">
      <div class="avatar" role="img" aria-label="Profielfoto medewerker" style="background:radial-gradient(circle at 50% 45%,#e5c4a8,#a98a70 60%,#8fa4b8 100%)"></div>
      <div class="name">Sanne Velders</div>
      <div class="dot orange"><svg width="14" height="14" viewBox="0 0 14 14"><circle cx="7" cy="7" r="5.8" fill="none" stroke="#fff" stroke-width="1.3"/><path d="M4.3 7.2l2 2 3.6-4" fill="none" stroke="#fff" stroke-width="1.3"/></svg></div>
      <div class="dot blue"><svg width="12" height="14" viewBox="0 0 12 14"><rect x="1" y="2" width="10" height="11.5" rx="1.5" fill="#fff"/><rect x="4" y="0.5" width="4" height="3" rx="1" fill="#fff" stroke="var(--blue)" stroke-width=".8"/><path d="M3.5 6.5h5M3.5 9h5M3.5 11.3h5" stroke="var(--blue)" stroke-width="1"/></svg></div>
    </div>
    <div class="abs row" style="top:393px">
      <div class="avatar" role="img" aria-label="Profielfoto medewerker" style="background:radial-gradient(circle at 50% 45%,#c8977a,#3a2a25 60%,#1c1614 100%)"></div>
      <div class="name">Iris Kampstra</div>
      <div class="dot orange"><svg width="14" height="14" viewBox="0 0 14 14"><circle cx="7" cy="7" r="5.8" fill="none" stroke="#fff" stroke-width="1.3"/><path d="M4.3 7.2l2 2 3.6-4" fill="none" stroke="#fff" stroke-width="1.3"/></svg></div>
      <div class="dot blue"><svg width="12" height="14" viewBox="0 0 12 14"><rect x="1" y="2" width="10" height="11.5" rx="1.5" fill="#fff"/><rect x="4" y="0.5" width="4" height="3" rx="1" fill="#fff" stroke="var(--blue)" stroke-width=".8"/><path d="M3.5 6.5h5M3.5 9h5M3.5 11.3h5" stroke="var(--blue)" stroke-width="1"/></svg></div>
    </div>
    <div class="abs row" style="top:479px">
      <div class="avatar" role="img" aria-label="Profielfoto medewerker" style="background:radial-gradient(circle at 50% 40%,#c9a38a,#4a3a33 70%)"></div>
      <div class="name">Roos van Dalen</div>
      <div class="dot orange"><svg width="14" height="14" viewBox="0 0 14 14"><circle cx="7" cy="7" r="5.8" fill="none" stroke="#fff" stroke-width="1.3"/><path d="M4.3 7.2l2 2 3.6-4" fill="none" stroke="#fff" stroke-width="1.3"/></svg></div>
      <div class="dot blue"><svg width="12" height="14" viewBox="0 0 12 14"><rect x="1" y="2" width="10" height="11.5" rx="1.5" fill="#fff"/><rect x="4" y="0.5" width="4" height="3" rx="1" fill="#fff" stroke="var(--blue)" stroke-width=".8"/><path d="M3.5 6.5h5M3.5 9h5M3.5 11.3h5" stroke="var(--blue)" stroke-width="1"/></svg></div>
    </div>
  </section>

  <section class="screen tasks">
    <svg class="abs menu" style="left:15px;top:25px" viewBox="0 0 17 12"><path d="M0 1h17M0 6h12M0 11h17" stroke="var(--ink)" stroke-width="1.6"/></svg>
    <div class="abs topbar-title" style="left:57px;top:22px">Lopende Taken</div>
    <svg class="abs" style="left:269px;top:24px" width="15" height="15" viewBox="0 0 15 15"><circle cx="6" cy="6" r="4.7" fill="none" stroke="var(--ink)" stroke-width="1.7"/><path d="M9.5 9.5L14 14" stroke="var(--ink)" stroke-width="1.8"/></svg>

    <div class="abs head-avatar" role="img" aria-label="Profielfoto Roos van Dalen"></div>
    <div class="abs head-name">Roos van Dalen</div>
    <div class="abs head-date">02-09-2018</div>
    <div class="abs dot blue head-check" style="margin:0"><svg width="14" height="14" viewBox="0 0 14 14"><circle cx="7" cy="7" r="5.8" fill="none" stroke="#fff" stroke-width="1.3"/><path d="M4.3 7.2l2 2 3.6-4" fill="none" stroke="#fff" stroke-width="1.3"/></svg></div>

    <svg width="0" height="0" style="position:absolute"><defs><clipPath id="inner"><circle cx="40" cy="40" r="35.5"/></clipPath></defs></svg>

    <!-- row 1 -->
    <div class="abs gauge" style="left:12px;top:161px">
      <svg width="80" height="80" viewBox="0 0 80 80"><circle cx="40" cy="40" r="37.5" fill="#fff" stroke="var(--blue)" stroke-width="3"/><path d="M0 40 L80 40 L80 80 L0 80Z" fill="var(--blue)" clip-path="url(#inner)"/></svg>
      <div class="pct">50%</div><div class="label">Schoonmaaktak en<br>shop algemeen</div>
    </div>
    <div class="abs gauge" style="left:109px;top:161px">
      <svg width="80" height="80" viewBox="0 0 80 80"><circle cx="40" cy="40" r="37.5" fill="#fff" stroke="var(--blue)" stroke-width="3"/><path d="M0 24 Q40 13 80 24 L80 80 L0 80Z" fill="var(--blue)" clip-path="url(#inner)"/></svg>
      <div class="pct">80%</div><div class="label">Schoonmaaktak en<br>Food Corner</div>
    </div>
    <div class="abs gauge" style="left:207px;top:161px">
      <svg width="80" height="80" viewBox="0 0 80 80"><circle cx="40" cy="40" r="37.5" fill="#fff" stroke="var(--blue)" stroke-width="3"/><path d="M0 12 Q40 2 80 12 L80 80 L0 80Z" fill="var(--blue)" clip-path="url(#inner)"/></svg>
      <div class="pct">95%</div><div class="label">Schoonmaaktak en<br>Magazijn, koel-en<br>vriescellen</div>
    </div>

    <!-- row 2 -->
    <div class="abs gauge" style="left:12px;top:302px">
      <svg width="80" height="80" viewBox="0 0 80 80"><circle cx="40" cy="40" r="37.5" fill="#fff" stroke="var(--blue)" stroke-width="3"/><path d="M0 40 L80 40 L80 80 L0 80Z" fill="var(--blue)" clip-path="url(#inner)"/></svg>
      <div class="pct">50%</div><div class="label">Schoonmaaktak en<br>Toiletten</div>
    </div>
    <div class="abs gauge" style="left:109px;top:302px">
      <svg width="80" height="80" viewBox="0 0 80 80"><circle cx="40" cy="40" r="37.5" fill="#fff" stroke="var(--blue)" stroke-width="3"/><path d="M0 12 Q40 2 80 12 L80 80 L0 80Z" fill="var(--blue)" clip-path="url(#inner)"/></svg>
      <div class="pct">95%</div><div class="label">Schoonmaaktak en<br>Food Corner</div>
    </div>
    <div class="abs gauge" style="left:207px;top:302px">
      <svg width="80" height="80" viewBox="0 0 80 80"><circle cx="40" cy="40" r="37.5" fill="#fff" stroke="var(--blue)" stroke-width="3"/><path d="M0 24 Q40 13 80 24 L80 80 L0 80Z" fill="var(--blue)" clip-path="url(#inner)"/></svg>
      <div class="pct">80%</div><div class="label">Schoonmaaktak en<br>Magazijn, koel-en<br>vriescellen</div>
    </div>

    <!-- row 3 -->
    <div class="abs gauge" style="left:12px;top:443px">
      <svg width="80" height="80" viewBox="0 0 80 80"><circle cx="40" cy="40" r="37.5" fill="#fff" stroke="var(--blue)" stroke-width="3"/><path d="M0 12 Q40 2 80 12 L80 80 L0 80Z" fill="var(--blue)" clip-path="url(#inner)"/></svg>
      <div class="pct">95%</div><div class="label">Schoonmaaktak en<br>shop algemeen</div>
    </div>
    <div class="abs gauge" style="left:109px;top:443px">
      <svg width="80" height="80" viewBox="0 0 80 80"><circle cx="40" cy="40" r="37.5" fill="#fff" stroke="var(--blue)" stroke-width="3"/><path d="M0 24 Q40 13 80 24 L80 80 L0 80Z" fill="var(--blue)" clip-path="url(#inner)"/></svg>
      <div class="pct">80%</div><div class="label">Schoonmaaktak en<br>Food Corner</div>
    </div>
    <div class="abs gauge" style="left:207px;top:443px">
      <svg width="80" height="80" viewBox="0 0 80 80"><circle cx="40" cy="40" r="37.5" fill="#fff" stroke="var(--blue)" stroke-width="3"/><path d="M0 40 L80 40 L80 80 L0 80Z" fill="var(--blue)" clip-path="url(#inner)"/></svg>
      <div class="pct">50%</div><div class="label">Schoonmaaktak en<br>Magazijn, koel-en<br>vriescellen</div>
    </div>
  </section>

</div>
</body>
</html>
```